Electrical Contracting business card design

We need a simple business card design for an Electrical Contracting business. A simple design would be appreciated
This company has 2 directors so on one it would have Dale Morrow & another with Shane Morrow.
Updates

Project Deadline Extended
Reason: Hello A few designers have asked for a logo unfortunately we don't have one so have extended deadline to see who can help us out with this. CHEERS

Project Deadline Extended
Reason: Waiting for business partner to return from xmas break. cheers

Industry/Entity Type

Business

Contact Information for Business Card

Quolvin Electrical Services P/L
REC: 63417
Residential Commercial Industrial
Service-Repairs-Renovations-Installations-Telephone-Data
Dale Morrow-Ph: 0437 612 388
Email: dale@quolvinelectrical.com.au

Requirements
Should not have
• The design should not have any electrical appliances in it ie: power-points, leads, houses etc.

```html
<!DOCTYPE html>
<html lang="en">
<head>
<meta charset="utf-8">
<title>Quolvin Electrical Services – Business Card</title>
<link href="https://fonts.googleapis.com/css2?family=Jost:wght@300;400&family=Oswald:wght@500&display=swap" rel="stylesheet">
<style>
  :root {
    --backdrop: #e4e1dc;
    --card-black: #121212;
    --accent-orange: #f28a1e;
    --detail-text: #d9892a;
    --band-text: #1a1a1a;
  }
  * { margin: 0; padding: 0; box-sizing: border-box; }
  html, body {
    width: 793px;
    height: 1200px;
    overflow: hidden;
    background: var(--backdrop);
  }
  .sheet {
    width: 793px;
    height: 1200px;
    display: flex;
    flex-direction: column;
    align-items: center;
    justify-content: center;
    gap: 90px;
  }
  .card {
    position: relative;
    width: 680px;
    height: 390px;
    background: var(--card-black);
    box-shadow: 0 6px 18px rgba(0,0,0,0.18);
    overflow: hidden;
  }
  /* Front: two directors */
  .card-front .directors {
    position: absolute;
    top: 52px;
    left: 0;
    right: 0;
    display: grid;
    grid-template-columns: 1fr 2px 1fr;
    column-gap: 54px;
    padding: 0 40px 0 60px;
  }
  .director {
    font-family: "Jost", sans-serif;
    font-weight: 300;
    color: var(--detail-text);
    font-size: 11.5px;
    line-height: 15.5px;
  }
  .director-left { text-align: right; }
  .director-right { text-align: left; }
  .director-name {
    font-size: 20px;
    line-height: 24px;
    font-weight: 400;
    color: var(--accent-orange);
  }
  .director-role { margin-bottom: 4px; }
  .divider {
    background: var(--accent-orange);
    width: 2px;
    height: 150px;
    margin-top: 8px;
  }
  .company-band {
    position: absolute;
    left: 0;
    right: 0;
    bottom: 0;
    height: 72px;
    background: var(--accent-orange);
    display: flex;
    align-items: center;
    justify-content: flex-end;
    padding-right: 32px;
  }
  .company-band .company-name {
    font-family: "Oswald", sans-serif;
    font-weight: 500;
    font-size: 15px;
    letter-spacing: 0.5px;
    text-transform: uppercase;
    color: var(--band-text);
  }
  /* Back: company name */
  .card-back {
    display: flex;
    align-items: center;
    justify-content: center;
  }
  .card-back .company-name {
    font-family: "Oswald", sans-serif;
    font-weight: 500;
    font-size: 20px;
    letter-spacing: 0.6px;
    text-transform: uppercase;
    color: var(--accent-orange);
  }
</style>
</head>
<body>
  <main class="sheet">
    <section class="card card-front" aria-label="Business card front">
      <div class="directors">
        <div class="director director-left">
          <p class="director-name">Dale Morrow</p>
          <p class="director-role">Directors</p>
          <p>0437 612 388</p>
          <p>Email: dale@quolvinelectrical.com.au</p>
          <p>P/L REC: 63417</p>
          <p>Residential Commercial</p>
          <p>Industrial/Service</p>
          <p>Repairs</p>
          <p>Renovations</p>
          <p>Installations</p>
          <p>Telephone</p>
          <p>Data</p>
        </div>
        <div class="divider"></div>
        <div class="director director-right">
          <p class="director-name">Shane Morrow</p>
          <p class="director-role">Directors</p>
          <p>0437 612 388</p>
          <p>Email: shane@quolvinelectrical.com.au</p>
          <p>P/L REC: 63417</p>
          <p>Residential Commercial</p>
          <p>Industrial/Service</p>
          <p>Repairs</p>
          <p>Renovations</p>
          <p>Installations</p>
          <p>Telephone</p>
          <p>Data</p>
        </div>
      </div>
      <div class="company-band">
        <p class="company-name">Quolvin Electrical Services</p>
      </div>
    </section>

    <section class="card card-back" aria-label="Business card back">
      <p class="company-name">Quolvin Electrical Services</p>
    </section>
  </main>
</body>
</html>
```